Email signature banner for companys 60th anniversary

We are a transportation company. This is what our website people came up with so far:

https://www.plandeckly.com/design/7xQwPz2LmN4rTbVc8HyUoK/Movren?node-id=1830-12

I want a picture of our transport truck with the decal on the back that we are putting on it.

Our website is www.movren.com

Target Market(s)

Customer recognition

Industry/Entity Type

fuel and oil distribution company

Requirements
Must have
• our 60th anniversary logo
Nice to have
• Delivering Energy to Build Communites.
Should not have
• picture of the guy from the current banner provided

```html
<!DOCTYPE html>
<html lang="en">
<head>
<meta charset="utf-8">
<title>Movren 60th Anniversary – Email Signature Banners</title>
<link rel="stylesheet" href="https://fonts.googleapis.com/css2?family=Oswald:wght@400;500;600&family=Poppins:wght@500;600&display=swap">
<style>
  :root {
    --board: #474747;
    --white: #ffffff;
    --brand-blue: #2a55a3;
    --soft-blue: #6f9ad8;
    --brand-red: #d42a2a;
    --ink: #111111;
    --sky: #4f7fc4;
    --sky-light: #9bb9e0;
    --sand: #d8ccb4;
    --sand-dark: #b59c7c;
  }
  * { box-sizing: border-box; margin: 0; padding: 0; }
  html, body { width: 1200px; height: 551px; overflow: hidden; background: var(--board); }
  .board { position: relative; width: 1200px; height: 551px; }

  .banner {
    position: absolute; width: 528px; height: 176px; overflow: hidden;
    background: var(--white); font-family: "Oswald", sans-serif;
  }
  .banner--a { left: 50px;  top: 84px; }
  .banner--b { left: 620px; top: 84px; }
  .banner--c { left: 50px;  top: 299px; }
  .banner--d { left: 620px; top: 299px; }

  .truck-photo {
    position: absolute; top: 0; left: 0; width: 100%; height: 100%;
    background: linear-gradient(180deg, var(--sky) 0%, var(--sky-light) 42%, var(--sand) 68%, var(--sand-dark) 100%);
  }
  .banner--a .truck-photo { width: 320px; clip-path: polygon(0 0, 290px 0, 240px 100%, 0 100%); }
  .banner--b .truck-photo { width: 277px; }

  .brand {
    position: absolute; display: flex; align-items: center; gap: 6px;
    font-family: "Oswald", sans-serif; font-weight: 600; font-size: 26px;
    color: var(--brand-blue); line-height: 1;
  }
  .brand__dot { width: 20px; height: 20px; border-radius: 50%; background: var(--brand-red); }

  .tagline {
    position: absolute; font-weight: 500; font-size: 23px; line-height: 1.18;
    letter-spacing: -0.3px;
  }
  .tagline--light { color: var(--white); }
  .tagline--blue { color: var(--brand-blue); }

  .anniv { position: absolute; color: var(--brand-blue); text-align: center; line-height: 1; }
  .anniv__num { font-weight: 500; }
  .est { font-family: "Poppins", sans-serif; color: var(--brand-red); font-size: 10px; letter-spacing: .5px; }

  .url {
    position: absolute; font-family: "Poppins", sans-serif; font-weight: 600;
    font-size: 11.5px; letter-spacing: 1.6px; color: var(--brand-blue);
  }

  .celebrate {
    position: absolute; right: 12px; top: 22px; color: var(--white);
    font-weight: 500; font-size: 19px; letter-spacing: -0.3px;
  }

  /* Banner A */
  .banner--a .brand { left: 385px; top: 18px; }
  .banner--a .anniv { left: 365px; top: 68px; width: 190px; }
  .banner--a .anniv__line { font-size: 23px; }
  .banner--a .anniv__num { font-size: 32px; }
  .banner--a .url { left: 360px; top: 148px; width: 200px; text-align: center; }

  /* Banner B */
  .big-sixty {
    position: absolute; font-weight: 600; color: var(--soft-blue); opacity: .85;
    font-size: 96px; line-height: 1; letter-spacing: -2px;
  }
  .banner--b .big-sixty { left: 342px; top: -4px; }
  .banner--b .brand { left: 412px; top: 38px; color: var(--brand-red); }
  .banner--b .anniv { left: 290px; top: 102px; width: 238px; font-size: 19px; }
  .banner--b .anniv__num { font-size: 26px; }
  .banner--b .est { display: block; margin-top: 4px; }
  .banner--b .url { left: 300px; top: 148px; width: 220px; text-align: center; }

  /* Banner C */
  .veil-c {
    position: absolute; inset: 0; background: rgba(255,255,255,.82);
    clip-path: polygon(0 0, 308px 0, 220px 100%, 0 100%);
  }
  .banner--c .big-sixty { left: 14px; top: -2px; font-size: 56px; color: var(--brand-blue); opacity: 1; font-style: normal; }
  .banner--c .brand { left: 168px; top: 20px; color: var(--brand-red); }
  .banner--c .anniv { left: 15px; top: 66px; color: var(--ink); text-align: left; font-size: 21px; }
  .banner--c .anniv__num { font-size: 30px; }
  .banner--c .est { position: absolute; left: 188px; top: 94px; }
  .banner--c .tagline { left: 13px; top: 108px; }
  .url-bar {
    position: absolute; right: 0; top: 138px; width: 140px; height: 22px;
    background: rgba(40,40,40,.55);
  }
  .banner--c .url { right: 14px; top: 141px; color: var(--white); }

  /* Banner D */
  .veil-d {
    position: absolute; inset: 0;
    background: linear-gradient(90deg, rgba(255,255,255,.85) 0%, rgba(255,255,255,.6) 38%, rgba(255,255,255,0) 62%);
  }
  .banner--d .brand { left: 14px; top: 20px; color: var(--brand-red); }
  .seal {
    position: absolute; left: 208px; top: 33px; width: 124px; height: 124px; border-radius: 50%;
    background: rgba(255,255,255,.78); color: var(--brand-blue); text-align: center;
    display: flex; flex-direction: column; justify-content: center; line-height: 1;
  }
  .seal__our { font-size: 21px; }
  .seal__num { font-size: 38px; font-weight: 500; }
  .seal__word { font-size: 15px; }
  .seal .est { margin-top: 3px; }
  .banner--d .tagline { left: 13px; top: 108px; }
  .url-bar--light { background: rgba(255,255,255,.6); width: 150px; top: 139px; }
  .banner--d .url { right: 20px; top: 142px; }
</style>
</head>
<body>
<main class="board">

  <section class="banner banner--a">
    <div class="truck-photo" role="img" aria-label="White fuel tanker truck parked on sand under a blue sky"></div>
    <p class="tagline tagline--light" style="left:12px; top:100px;">Delivering Energy to<br>Build Communities</p>
    <div class="brand"><span class="brand__dot"></span>Movren</div>
    <div class="anniv">
      <div class="anniv__line">Our <span class="anniv__num">60th</span></div>
      <div class="anniv__line">Anniversary</div>
      <div class="est">EST. 1965</div>
    </div>
    <p class="url">www.movren.com</p>
  </section>

  <section class="banner banner--b">
    <div class="truck-photo" role="img" aria-label="White fuel tanker truck parked on sand under a blue sky"></div>
    <p class="tagline tagline--light" style="left:12px; top:100px;">Delivering Energy to<br>Build Communities</p>
    <div class="big-sixty">60</div>
    <div class="brand"><span class="brand__dot"></span>Movren</div>
    <div class="anniv">Our <span class="anniv__num">60th</span> Anniversary<span class="est">EST. 1965</span></div>
    <p class="url">www.movren.com</p>
  </section>

  <section class="banner banner--c">
    <div class="truck-photo" role="img" aria-label="White fuel tanker truck on a sandy work site under a blue sky"></div>
    <div class="veil-c"></div>
    <div class="big-sixty">60</div>
    <div class="brand"><span class="brand__dot"></span>Movren</div>
    <div class="anniv">Our <span class="anniv__num">60th</span> Anniversary</div>
    <span class="est">EST. 1965</span>
    <p class="tagline tagline--blue">Delivering Energy to<br>Build Communities</p>
    <p class="celebrate">Celebrating 60 years</p>
    <div class="url-bar"></div>
    <p class="url">www.movren.com</p>
  </section>

  <section class="banner banner--d">
    <div class="truck-photo" role="img" aria-label="White fuel tanker truck on a sandy work site under a blue sky"></div>
    <div class="veil-d"></div>
    <div class="brand"><span class="brand__dot"></span>Movren</div>
    <div class="seal">
      <span class="seal__our">Our</span>
      <span class="seal__num">60th</span>
      <span class="seal__word">Anniversary</span>
      <span class="est">EST. 1965</span>
    </div>
    <p class="tagline tagline--blue">Delivering Energy to<br>Build Communities</p>
    <p class="celebrate">Celebrating 60 years</p>
    <div class="url-bar url-bar--light"></div>
    <p class="url">www.movren.com</p>
  </section>

</main>
</body>
</html>
```